Shabby Shic / Elegant - Web branding and elements needed

Just need a design that has all elements I will need to build out an existing template. Attaching designs that we like and want to be similar in feel to... Also attaching the barebones current template that I need to add the elements to. Anything on there can be modified, just using it for layout so you can use that as a template. In addition, feel free to play with the logo to see if there is a diffrent styl (Perhaps a more flat style).

Target Market(s)

Middle age woman, grandmothers, mothers

Industry/Entity Type

Fashion

Number of Pages Required

3 page

Font styles to use
Sans Serif
Decorative
Script

Colors

Designer to choose colors to be used in the design.

Requirements
Must have
• Easy to see. Fits with demographic.
Should not have
• Just standard, corporate feel

```html
<!DOCTYPE html>
<html lang="en">
<head>
<meta charset="utf-8">
<title>Stitchbloom – Home</title>
<link href="https://fonts.googleapis.com/css2?family=Raleway:wght@400;500;600&family=Roboto:wght@400;500;700&family=Lobster+Two:ital,wght@1,700&family=Kaushan+Script&display=swap" rel="stylesheet">
<style>
:root{
  --green:#6cb33f;
  --green-line:#9fcf6b;
  --pink:#ec2f7f;
  --pink-soft:#f5c6d8;
  --orange:#f47a1e;
  --orange-dark:#df620f;
  --grey-panel:#dcdcdc;
  --grey-card:#f1f1f1;
  --grey-tab:#8e8e8e;
  --footer:#d3d3d3;
  --text:#333;
  --muted:#777;
  --white:#fff;
}
*{box-sizing:border-box;margin:0;padding:0}
html,body{width:1200px;height:2378px;overflow:hidden}
body{position:relative;background:var(--white);font-family:"Roboto",sans-serif;color:var(--text)}
a{color:inherit;text-decoration:none}
.abs{position:absolute}

/* top bar */
.topbar{left:0;top:0;width:1200px;height:35px;background:var(--green);color:var(--white);font:400 12px "Raleway",sans-serif;display:flex;align-items:center;justify-content:space-between;padding:0 98px}
.topbar .links{display:flex;gap:14px;align-items:center}
.topbar .dot{width:10px;height:10px;border-radius:50%;background:rgba(255,255,255,.7)}

/* header */
.header{left:0;top:35px;width:1200px;height:114px;background:#fbf6f0}
.brand{left:98px;top:38px;display:flex;align-items:center;gap:12px;font:600 40px "Raleway",sans-serif;color:var(--pink)}
.brand .mark{width:22px;height:22px;border-radius:50%;background:var(--green)}
.search{left:528px;top:36px;width:402px;height:40px;display:flex;border:1px solid #ddd;border-radius:4px;overflow:hidden;background:var(--white)}
.search span{flex:1;padding:0 16px;font:400 12px "Raleway",sans-serif;color:#999;line-height:38px}
.search b{width:88px;background:var(--orange);color:var(--white);font:500 15px "Raleway",sans-serif;text-align:center;line-height:38px}
.account{left:972px;top:30px;font:600 15px "Raleway",sans-serif;color:var(--pink);line-height:34px}
.account div{display:flex;align-items:center;gap:8px}
.account svg{fill:var(--orange)}

/* nav */
.nav{left:0;top:149px;width:1200px;height:41px;background:var(--pink);display:flex;align-items:center;padding-left:98px;gap:36px;color:var(--white);font:500 15.5px "Raleway",sans-serif;letter-spacing:.6px}

/* hero */
.hero{left:0;top:190px;width:1200px;height:412px;background:linear-gradient(180deg,#f0c8d9 0%,#dcd3c8 55%,#b9d9a4 100%)}
.hero-kicker{left:98px;top:312px;font:400 29px "Raleway",sans-serif;letter-spacing:5px;color:var(--green)}
.hero-title{left:194px;top:343px;font:700 italic 68px "Lobster Two",sans-serif;color:var(--pink);letter-spacing:1px}
.hero-btn{left:258px;top:433px;width:210px;height:43px;background:var(--orange);color:var(--white);border-radius:4px;font:500 21px "Raleway",sans-serif;letter-spacing:4px;text-align:center;line-height:43px}
.hero-photo{left:720px;top:210px;width:360px;height:380px}

/* about */
.divider{left:98px;width:1002px;height:30px}
.about-title{left:0;width:1200px;top:656px;text-align:center;font:400 33px "Kaushan Script",cursive;color:var(--pink)}
.about-text{left:98px;top:708px;width:1002px;text-align:center;font:400 16.5px/26px "Roboto",sans-serif;letter-spacing:.5px;color:var(--text)}

/* tabs */
.tabs{left:98px;top:951px;display:flex;height:47px}
.tab{height:47px;line-height:47px;text-align:center;font:500 18px "Raleway",sans-serif;letter-spacing:3px;color:var(--white)}
.tab.active{width:241px;background:var(--pink);border-radius:6px 0 0 6px}
.tab.idle{width:317px;background:var(--grey-tab);border-radius:0 6px 6px 0}

/* products */
.grid{left:98px;top:1026px;display:grid;grid-template-columns:repeat(3,203px);grid-auto-rows:290px;column-gap:26px;row-gap:29px}
.card{background:var(--grey-card);border-radius:6px;box-shadow:0 2px 4px rgba(0,0,0,.18);position:relative;text-align:center}
.card .thumb{position:absolute;left:36px;top:17px;width:131px;height:131px;border:1px solid #ddd;background:linear-gradient(180deg,#fff 0%,#f2f6ea 60%,#fbe6df 100%)}
.card .name{position:absolute;left:8px;right:8px;top:166px;font:500 13px/17px "Roboto",sans-serif;color:var(--pink)}
.card .price{position:absolute;left:0;right:0;top:206px;font:500 24px "Roboto",sans-serif;color:var(--orange)}
.card .price s{font-size:13px;color:var(--muted);margin-right:8px;vertical-align:3px}
.card .cart{position:absolute;left:0;right:0;bottom:0;height:44px;border-top:1px solid #ccc;line-height:44px;font:700 15.5px "Roboto",sans-serif;color:var(--green)}
.card .cart.on{background:var(--green);color:var(--white);border-radius:0 0 6px 6px;border-top:none}

/* sidebar */
.panel{left:785px;width:315px;background:var(--grey-panel);border-radius:6px;box-shadow:0 2px 4px rgba(0,0,0,.15);overflow:hidden}
.panel-head{height:51px;background:var(--orange-dark);text-align:center;line-height:51px;font:400 24px "Kaushan Script",cursive;color:var(--white);letter-spacing:1px}
.top-one{position:absolute;left:17px;top:68px;width:282px;height:257px;background:var(--white);border-radius:6px;text-align:center}
.top-one .thumb{position:absolute;left:74px;top:17px;width:131px;height:131px;border:1px solid #ddd;background:linear-gradient(180deg,#fff,#eef0f8)}
.top-one .name{position:absolute;left:0;right:0;top:163px;font:400 15.5px/21px "Roboto",sans-serif}
.top-one .price{position:absolute;left:0;right:0;top:214px;font:500 19px "Roboto",sans-serif;color:var(--orange)}
.rank{position:absolute;width:34px;height:34px;border-radius:50%;border:2px solid var(--pink);color:var(--pink);background:#f7dbe7;font:700 19px/30px "Roboto",sans-serif;text-align:center}
.seller{position:absolute;left:17px;display:flex;gap:22px;align-items:center}
.seller .txt{font:400 13px/19px "Roboto",sans-serif}
.seller .txt b{display:block;font:500 16.5px "Roboto",sans-serif;color:var(--orange)}
.news-sub{position:absolute;left:17px;top:68px;font:400 16px "Roboto",sans-serif;color:var(--pink)}
.news-txt{position:absolute;left:17px;top:96px;width:222px;font:400 12px/16px "Roboto",sans-serif}
.news-icon{position:absolute;right:0;top:56px;width:78px;height:90px}
.news-input{position:absolute;left:17px;top:162px;width:282px;height:40px;background:var(--white);border-radius:8px;padding-left:16px;line-height:40px;font:400 15px "Roboto",sans-serif;color:#444}
.news-btn{position:absolute;left:17px;top:226px;width:282px;height:40px;background:var(--pink);border-radius:4px;text-align:center;line-height:40px;color:var(--white);font:500 16px "Roboto",sans-serif;letter-spacing:1px}

/* pagination */
.pager{left:0;width:1248px;top:1994px;text-align:center;font:500 16px "Roboto",sans-serif;color:var(--muted)}
.pager .cur{color:var(--pink)}
.pager .next{color:var(--pink)}

/* footer */
.footer{left:0;top:2056px;width:1200px;height:271px;background:var(--footer)}
.footer-brand{left:98px;top:2100px;display:flex;align-items:center;gap:10px;font:600 34px "Raleway",sans-serif;color:var(--pink)}
.footer-brand .mark{width:18px;height:18px;border-radius:50%;background:var(--green)}
.footer-about{left:98px;top:2193px;width:330px;font:400 12.5px/19px "Roboto",sans-serif;color:#333}
.fcol{top:2094px}
.fcol h4{font:500 15px "Roboto",sans-serif;color:var(--pink);letter-spacing:.6px;margin-bottom:8px}
.fcol li{list-style:none;font:400 12.5px/19.2px "Roboto",sans-serif;color:#333}
.field{position:absolute;left:870px;width:230px;background:var(--white);border-radius:6px;padding:10px 12px;font:400 12.5px "Roboto",sans-serif;color:#333}
.send{position:absolute;left:1070px;top:2224px;width:30px;height:66px;background:var(--pink);border-radius:0 6px 6px 0;color:var(--white);font:700 10px/12px "Roboto",sans-serif;text-align:center;padding-top:8px}
.bottom{left:0;top:2327px;width:1200px;height:51px;background:var(--pink);color:var(--white);font:500 12.5px "Roboto",sans-serif;padding-left:98px;line-height:51px}
.social{left:987px;top:2336px;display:flex;gap:9px}
.social span{width:33px;height:33px;border-radius:50%;background:var(--green)}
</style>
</head>
<body>

<div class="abs topbar">
  <span>Currency: $ Dollar ▾</span>
  <div class="links"><span>Register</span><i class="dot"></i><span>Login</span><i class="dot"></i><span>Delivery</span><i class="dot"></i><span>Checkout</span></div>
</div>

<header class="abs header"></header>
<div class="abs brand"><span class="mark"></span>Stitchbloom</div>
<div class="abs search"><span>Search entire store here...</span><b>SEARCH</b></div>
<div class="abs account">
  <div><svg width="14" height="14" viewBox="0 0 14 14"><circle cx="7" cy="4" r="3.5"/><path d="M0 14c0-4 3-6 7-6s7 2 7 6z"/></svg>MY ACCOUNT</div>
  <div><svg width="18" height="14" viewBox="0 0 18 14"><path d="M0 1h3l2 9h10l2-7H5" fill="none" stroke="#f47a1e" stroke-width="2"/><circle cx="7" cy="12.5" r="1.5"/><circle cx="14" cy="12.5" r="1.5"/></svg>CART (0)</div>
</div>

<nav class="abs nav">
  <svg width="18" height="16" viewBox="0 0 18 16" fill="#fff"><path d="M9 0l9 8h-3v8h-4v-5H7v5H3V8H0z"/></svg>
  <span>NEW RELEASES</span><span>FEATURED PRODUCTS</span><span>ACCENTS</span><span>ALPHABATES &amp; LETTERING</span><span>APPLIQUE</span><span>ALL CATEGORIES</span>
</nav>

<section class="abs hero"></section>
<div class="abs hero-kicker">CREATE &amp; EMBELLISH YOUR</div>
<div class="abs hero-title">memories</div>
<div class="abs hero-btn">SHOP NOW</div>
<svg class="abs hero-photo" viewBox="0 0 360 380" role="img" aria-label="Cupcakes with sprinkles and embroidered toppers framed by pastel flower petals">
  <defs><radialGradient id="ph" cx="50%" cy="45%" r="60%"><stop offset="0" stop-color="#f6f0e6"/><stop offset=".6" stop-color="#d9b47a"/><stop offset="1" stop-color="#a88a5c"/></radialGradient></defs>
  <circle cx="163" cy="205" r="150" fill="#ed8fb6" opacity=".55"/>
  <circle cx="163" cy="205" r="128" fill="url(#ph)"/>
</svg>

<svg class="abs divider" style="top:662px" viewBox="0 0 1002 30"><line x1="22" y1="15" x2="980" y2="15" stroke="var(--green-line)" stroke-width="1.5"/><circle cx="11" cy="15" r="10" fill="var(--green-line)"/><circle cx="991" cy="15" r="10" fill="var(--green-line)"/><rect x="400" y="0" width="202" height="30" fill="#fff"/></svg>
<h2 class="abs about-title">ABOUT US</h2>
<p class="abs about-text">Lorem Ipsum is simply dummy text of the printing and typesetting industry. Lorem Ipsum has been the industry's standard dummy text ever since the 1500s, when an unknown printer took a galley of type and scrambled it to make a type specimen book. It has survived not only five centuries, but also the leap into electronic typesetting, remaining essentially unchanged. It was popularised in the 1960s with the release of Letraset sheets containing Lorem Ipsum passages, and more recently with desktop publishing software like Aldus PageMaker including versions of Lorem Ipsum.</p>
<svg class="abs divider" style="top:857px" viewBox="0 0 1002 30"><line x1="22" y1="15" x2="980" y2="15" stroke="var(--green-line)" stroke-width="1.5"/><circle cx="11" cy="15" r="10" fill="var(--green-line)"/><circle cx="991" cy="15" r="10" fill="var(--green-line)"/></svg>

<div class="abs tabs"><div class="tab active">NEW ARRIVALS</div><div class="tab idle">FEATURED PRODUCTS</div></div>

<div class="abs grid">
  <div class="card"><div class="thumb" role="img" aria-label="Embroidery design preview"></div><div class="name">Rosa Monogram Font - Elegant Script Font</div><div class="price"><s>$7.49</s>$3.74</div><div class="cart">ADD TO CART</div></div>
  <div class="card"><div class="thumb" role="img" aria-label="Embroidery design preview"></div><div class="name">Rosa Monogram Font - Elegant Script Font</div><div class="price"><s>$7.49</s>$3.74</div><div class="cart on">ADD TO CART</div></div>
  <div class="card"><div class="thumb" role="img" aria-label="Embroidery design preview"></div><div class="name">Rosa Monogram Font - Elegant Script Font</div><div class="price"><s>$7.49</s>$3.74</div><div class="cart">ADD TO CART</div></div>
  <div class="card"><div class="thumb" role="img" aria-label="Embroidery design preview"></div><div class="name">Rosa Monogram Font - Elegant Script Font</div><div class="price"><s>$7.49</s>$3.74</div><div class="cart">ADD TO CART</div></div>
  <div class="card"><div class="thumb" role="img" aria-label="Embroidery design preview"></div><div class="name">Rosa Monogram Font - Elegant Script Font</div><div class="price"><s>$7.49</s>$3.74</div><div class="cart">ADD TO CART</div></div>
  <div class="card"><div class="thumb" role="img" aria-label="Embroidery design preview"></div><div class="name">Rosa Monogram Font - Elegant Script Font</div><div class="price"><s>$7.49</s>$3.74</div><div class="cart">ADD TO CART</div></div>
  <div class="card"><div class="thumb" role="img" aria-label="Embroidery design preview"></div><div class="name">Rosa Monogram Font - Elegant Script Font</div><div class="price"><s>$7.49</s>$3.74</div><div class="cart">ADD TO CART</div></div>
  <div class="card"><div class="thumb" role="img" aria-label="Embroidery design preview"></div><div class="name">Rosa Monogram Font - Elegant Script Font</div><div class="price"><s>$7.49</s>$3.74</div><div class="cart">ADD TO CART</div></div>
  <div class="card"><div class="thumb" role="img" aria-label="Embroidery design preview"></div><div class="name">Rosa Monogram Font - Elegant Script Font</div><div class="price"><s>$7.49</s>$3.74</div><div class="cart">ADD TO CART</div></div>
</div>

<aside class="abs panel" style="top:951px;height:682px">
  <div class="panel-head">OUR TOP SELLERS</div>
  <div class="top-one">
    <div class="thumb" role="img" aria-label="Script alphabet font sample"></div>
    <div class="rank" style="left:231px;top:12px">1</div>
    <div class="name">Rosa Monogram Font - Elegant<br>Script Font</div>
    <div class="price">$3.74</div>
  </div>
  <div class="seller" style="top:344px"><span class="rank" style="position:static">2</span><div class="txt">Sweet As Sugar Lace Border Design<b>$1.74</b></div></div>
  <div class="seller" style="top:434px"><span class="rank" style="position:static">3</span><div class="txt">Sweet As Sugar Lace Border Design<b>$1.74</b></div></div>
  <div class="seller" style="top:523px"><span class="rank" style="position:static">4</span><div class="txt">Sweet As Sugar Lace Border Design<b>$1.74</b></div></div>
  <div class="seller" style="top:613px"><span class="rank" style="position:static">5</span><div class="txt">Sweet As Sugar Lace Border Design<b>$1.74</b></div></div>
</aside>

<aside class="abs panel" style="top:1664px;height:290px">
  <div class="panel-head">NEWSLETTER</div>
  <svg class="news-icon" viewBox="0 0 78 90"><rect x="8" y="6" width="70" height="84" rx="4" fill="#c9c9c9"/><rect x="20" y="20" width="24" height="20" fill="#e6e6e6"/><rect x="50" y="22" width="20" height="4" fill="#e6e6e6"/><rect x="50" y="32" width="20" height="4" fill="#e6e6e6"/><rect x="20" y="50" width="50" height="4" fill="#e6e6e6"/><rect x="20" y="60" width="50" height="4" fill="#e6e6e6"/></svg>
  <div class="news-sub">SUBSCRIBE OUR NEWSLETTER</div>
  <p class="news-txt">Lorem Ipsum is simply dummy text of the printing and typesetting total industry.</p>
  <div class="news-input">Email</div>
  <div class="news-btn">SUBSCRIBE</div>
</aside>

<div class="abs pager">« PREVIOUS &nbsp; 1 <span class="cur">2</span> 3 4 5..............10 &nbsp;<span class="next">NEXT »</span></div>

<footer class="abs footer"></footer>
<div class="abs footer-brand"><span class="mark"></span>Stitchbloom</div>
<p class="abs footer-about">There are many variations of passages of Lorem Ipsum available, but the majority have suffered alteration in some form, by injected humour, or randomised words which don't look even slightly believable. There are many variations of passages of Lorem Ipsum available, but the majority have suffered.</p>
<div class="abs fcol" style="left:496px"><h4>QUICK LINKS</h4><ul><li>Home</li><li>Cart</li><li>Register</li><li>Wishlist</li><li>Checkout</li><li>My Account</li><li>Terms &amp; Conditions</li><li>Privacy Policy</li><li>Refund Policy</li></ul></div>
<div class="abs fcol" style="left:667px"><h4>CATEGORIES</h4><ul><li>New Releases</li><li>Featured Products</li><li>Accents</li><li>Alphabates &amp; Lettering</li><li>Applique</li><li>Font Frames</li><li>In The Hoop</li><li>Words &amp; Phrases</li><li>All Categories</li></ul></div>
<div class="abs fcol" style="left:870px"><h4>CONTACT FORM</h4></div>
<div class="field" style="top:2129px;height:33px">Name</div>
<div class="field" style="top:2176px;height:34px">Email</div>
<div class="field" style="top:2224px;height:66px">Message</div>
<div class="send">S<br>E<br>N<br>D</div>

<div class="abs bottom">© 2017 Stitchbloom &nbsp;|&nbsp; All Rights Reserved.</div>
<div class="abs social"><span></span><span></span><span></span></div>

</body>
</html>
```